Domestic violence resource cards for distribution to at-risk patients in an emergency department

Using the attached image(or very similar) and text document, a tri-fold business card is requested that integrates the image on the outside and the document content throughout the card's remaining faces. A creative format is requested, one that does not look like the typical cold, uncaring bullet point outlines that are found in similar resource projects. Bold or larger font sizes are requested for headings and body text is not required to be aligned or justified and the bullet points in the supplied document can be removed for creative license. Palattes should be clear, avoiding neons or implied target gender. Legibility is paramount, but again a creative presentation of a very serious subject is our goal. These cards are intended to be distributed to patients or others in the emergency department that may benefit from domestic violence resources. The business card size is mandatory so that the card can be concealed if needed by the receiver.
Updates

Reason: There are several revisions from designers that we are anxiously awaiting; we want to provide time for these designers to submit new designs but also continue spending time with their families and friends around the holiday season.

Target Market(s)

Patients and family in contact with emergency services

Industry/Entity Type

Healthcare

Contact Information for Business Card

Double sided tri-fold card with image on outer sides, text content and resource phone numbers on the exterior. When complete, the card should fold to standard US business card size.

Font styles to use
Other font styles liked:
• Designer's choice, but clear and legible

Requirements
Must have
• See above description. Card must be tri-fold, fold down to standard business card size, remain easily readable, and fold along the long edge.
Should not have
• Cartoon images; bloated fonts or clipart; bright, flashy neon or rainbow-like colors; additional graphics or charts.

```html
<!DOCTYPE html>
<html lang="en">
<head>
<meta charset="utf-8">
<title>Domestic Violence Resource Card</title>
<link href="https://fonts.googleapis.com/css2?family=Mulish:ital,wght@0,400;0,700;1,600;1,800&family=Carlito:ital,wght@0,400;0,700;1,400;1,700&display=swap" rel="stylesheet">
<style>
  :root {
    --backdrop: #e9e5df;
    --card: #f4f1ee;
    --card-shade: #e6e1dc;
    --ink: #1e1e1e;
    --ink-soft: #3a3a3a;
    --label: #444;
    --fold: #cfc8c1;
    --photo-dark: #141414;
    --photo-mid: #6b625a;
    --photo-light: #b9aea3;
  }
  * { box-sizing: border-box; margin: 0; padding: 0; }
  html, body { width: 1200px; height: 579px; overflow: hidden; }
  body {
    background: var(--backdrop);
    color: var(--ink);
    font-family: "Carlito", "Calibri", sans-serif;
    display: flex;
    justify-content: space-around;
    padding: 8px 40px 0;
  }
  .side { display: flex; flex-direction: column; align-items: center; }
  .side-label {
    font-family: "Mulish", sans-serif;
    font-size: 22px;
    color: var(--label);
    height: 36px;
    line-height: 36px;
  }
  .card {
    width: 480px;
    display: flex;
    flex-direction: column;
    box-shadow: 0 4px 14px rgba(0,0,0,.18);
  }
  .panel {
    height: 176px;
    background: radial-gradient(ellipse at center, var(--card) 55%, var(--card-shade) 100%);
    border-bottom: 1px solid var(--fold);
    position: relative;
    overflow: hidden;
  }
  .panel:last-child { border-bottom: none; }
  .flipped > .panel-body { transform: rotate(180deg); height: 100%; }

  /* Outside: hotlines */
  .hotlines {
    height: 100%;
    display: flex; flex-direction: column; justify-content: center;
    text-align: center; gap: 4px;
    font-family: "Mulish", sans-serif;
  }
  .hotline-name { font-style: italic; font-weight: 600; font-size: 12.5px; }
  .hotline-number { font-style: italic; font-weight: 800; font-size: 12.5px; letter-spacing: .5px; margin-bottom: 4px; }

  /* Outside: photo */
  .photo {
    height: 100%;
    background:
      radial-gradient(ellipse 32% 70% at 50% 55%, var(--photo-light) 0%, var(--photo-mid) 45%, transparent 80%),
      linear-gradient(90deg, #f0ece8 0%, var(--photo-dark) 22%, var(--photo-dark) 78%, #f0ece8 100%);
  }

  /* Safety tips */
  .tips {
    list-style: none;
    font-family: "Mulish", sans-serif;
    font-style: italic;
    font-size: 11.5px;
    line-height: 1.45;
    padding: 18px 30px;
  }
  .tips li::before, .reminders li::before, .warning-signs li::before { content: "· "; }

  /* Inside: warning signs */
  .warning {
    height: 100%;
    display: flex; flex-direction: column; justify-content: center;
    padding: 6px 22px;
    font-style: italic;
    font-size: 11.5px;
    line-height: 1.13;
  }
  .warning-title { text-align: center; font-weight: 700; font-size: 12.5px; margin-bottom: 2px; }
  .warning-signs { list-style: none; }
  .warning-verdict { text-align: right; font-weight: 700; font-size: 12.5px; margin-top: 3px; }

  /* Inside: reminders */
  .remember { padding: 10px 30px; font-size: 12.5px; line-height: 1.3; }
  .remember-title { text-align: center; font-weight: 700; font-size: 13px; margin-bottom: 3px; }
  .reminders { list-style: none; color: var(--ink-soft); }

  /* Inside: local resources */
  .resources {
    height: 100%;
    display: flex; flex-direction: column; justify-content: center;
    text-align: center; gap: 3px;
    font-family: "Mulish", sans-serif;
    font-size: 12.5px;
  }
  .resource-name { font-style: italic; font-weight: 600; }
  .resource-number { font-weight: 800; letter-spacing: .5px; margin-bottom: 5px; }
  .resource-web { font-weight: 700; margin-top: 4px; }
</style>
</head>
<body>
  <section class="side side-outside">
    <h2 class="side-label">Outside</h2>
    <div class="card">
      <div class="panel">
        <div class="hotlines">
          <p class="hotline-name">Harbor Line Domestic Violence Hotline</p>
          <p class="hotline-number">1-800-555-0142</p>
          <p class="hotline-name">Safe Haven Shelter: Domestic Violence Crisis Resource</p>
          <p class="hotline-number">303-555-0187</p>
          <p class="hotline-name">Pathway Domestic Violence Resources</p>
          <p class="hotline-number">303-555-0126</p>
          <p class="hotline-name">The Open Door Center</p>
          <p class="hotline-number">1-888-555-0193</p>
        </div>
      </div>
      <div class="panel">
        <div class="photo" role="img" aria-label="Photograph of two clenched hands bound together at the wrists with rope"></div>
      </div>
      <div class="panel flipped">
        <div class="panel-body">
          <ul class="tips">
            <li>Seek help at a police station if you are in an abusive situation</li>
            <li>Be careful: you are most at risk when leaving</li>
            <li>Review your plan often before emergencies</li>
            <li>Keep a charged phone hidden until you are safe</li>
            <li>Open a private bank account</li>
            <li>Do not share your location online</li>
            <li>Stay private online and clear your call history</li>
          </ul>
        </div>
      </div>
    </div>
  </section>

  <section class="side side-inside">
    <h2 class="side-label">Inside</h2>
    <div class="card">
      <div class="panel">
        <div class="warning">
          <h3 class="warning-title">DOES YOUR PARTNER EVER...</h3>
          <ul class="warning-signs">
            <li>Hit, kick, push, choke or slap you?</li>
            <li>Intimidate you with weapons or harmful objects?</li>
            <li>Force you to engage in sexual acts?</li>
            <li>Threaten to hurt you, your children or your friends/family?</li>
            <li>Threaten to deport you or tell others your personal information?</li>
            <li>Control where you go, who you talk to or who you make friends with?</li>
            <li>Keep, hide or destroy your most important things?</li>
            <li>Blame, embarrass, or criticize you, make you feel worthless or guilty?</li>
            <li>Control your food, money, medicines or medical care?</li>
          </ul>
          <p class="warning-verdict">You may be a victim of abuse or neglect!</p>
        </div>
      </div>
      <div class="panel">
        <div class="remember">
          <h3 class="remember-title">ALWAYS REMEMBER...</h3>
          <ul class="reminders">
            <li>You have a right to be safe anywhere</li>
            <li>You don't deserve to be hit or threatened</li>
            <li>Your children deserve a safe home</li>
            <li>You have a right to leave</li>
            <li>You are not alone</li>
            <li>You have choices and support</li>
            <li>Know where your nearest shelter is</li>
            <li>Tell someone you trust what is happening</li>
          </ul>
        </div>
      </div>
      <div class="panel flipped">
        <div class="panel-body">
          <div class="resources">
            <p class="resource-name">Oak Root Violence Resources</p>
            <p class="resource-number">303-555-0164</p>
            <p class="resource-name">Quiet Harbor: Sexual Assault Victim's Advocate</p>
            <p class="resource-number">303-555-0178</p>
            <p class="resource-name">Kind Hearts: Teen Dating Resource</p>
            <p class="resource-number">1-866-555-0151<br>or text "kind" to 55501</p>
            <p class="resource-web">www.safehomefinder.org</p>
          </div>
        </div>
      </div>
    </div>
  </section>
</body>
</html>
```